New baby product company needs product trifold

We are a new company with products based from 30+ years of nursing experience with babies. Most of our products are made from 100% organic materials. We need a product brochure to place in waiting rooms of Labor and delivery doctors and birthing centers. The front page needs to grab their attention and invite them to pick it up and read more. Target audience expecting and new mothers ages 22-39. The final design should communicate our expertise and experience of knowing what a baby needs.
Need extra days to review
Baby

```html
<!DOCTYPE html>
<html lang="en">
<head>
<meta charset="utf-8">
<title>Nestling Baby Products – Trifold Brochure</title>
<link rel="stylesheet" href="https://fonts.googleapis.com/css2?family=Lato:wght@400;700&family=Marcellus&display=swap">
<style>
  :root {
    --bg: #6f6b6b;
    --paper: #f3f3f2;
    --paper-edge: #e4e4e3;
    --blue: #1f64b0;
    --sky: #3d98d6;
    --navy: #154a8e;
    --green: #7ab929;
    --green-dark: #3f9b35;
    --ink: #2b2b2b;
    --photo-baby: #b9b4ae;
    --photo-room: #cfc9c0;
    --photo-nest: #ece6dc;
  }
  * { box-sizing: border-box; margin: 0; padding: 0; }
  html, body { width: 1200px; height: 906px; overflow: hidden; background: var(--bg); }
  body { position: relative; font-family: "Lato", sans-serif; color: var(--ink); }

  .brochure {
    position: absolute; left: 110px; top: 73px;
    width: 981px; height: 760px;
    display: flex; background: var(--paper);
  }
  .panel { position: relative; width: 327px; height: 760px; overflow: hidden; }
  .panel + .panel { border-left: 1px solid var(--paper-edge); }

  .wave-art { position: absolute; left: 0; top: 0; width: 654px; height: 760px; z-index: 1; }
  .panel-art { position: absolute; inset: 0; }

  .heading {
    font-family: "Marcellus", serif; font-size: 24px; color: var(--blue);
    position: absolute; z-index: 2;
  }
  .heading::after {
    content: ""; display: block; width: 96px; height: 3px;
    background: var(--green-dark); margin-top: 6px;
  }
  .body-copy {
    position: absolute; z-index: 2; font-size: 13px; line-height: 1.38; color: var(--ink);
  }

  .intro .heading { left: 96px; top: 34px; }
  .intro .body-copy { left: 96px; top: 82px; width: 200px; }

  .mission .heading { left: 44px; top: 112px; }
  .mission .body-copy { left: 44px; top: 158px; width: 250px; }

  .social { position: absolute; left: 40px; top: 560px; width: 250px; text-align: center; z-index: 2; }
  .social-title { font-family: "Marcellus", serif; color: var(--blue); font-size: 16px; margin-bottom: 6px; }
  .social-line { font-size: 12px; display: flex; align-items: center; justify-content: center; gap: 6px; margin-bottom: 3px; }
  .social-dot { width: 10px; height: 10px; border-radius: 50%; background: var(--navy); display: inline-block; }

  .web { font-family: "Marcellus", serif; font-size: 17px; color: var(--ink); position: absolute; z-index: 2; width: 100%; text-align: center; }
  .web b { color: var(--blue); font-weight: 400; }
  .intro .web { top: 640px; }
  .mission .web { top: 686px; }
  .cover .web { top: 690px; }

  .foot-bar { position: absolute; left: 30px; right: 30px; bottom: 36px; height: 6px; background: var(--green-dark); z-index: 2; }

  .brand { position: absolute; z-index: 2; display: flex; align-items: center; gap: 10px; }
  .brand-mark { border-radius: 50%; background: var(--sky); flex: none; }
  .brand-name { font-family: "Lato", sans-serif; font-weight: 700; color: var(--blue); line-height: 1; }
  .brand-name small { display: block; font-size: 0.42em; letter-spacing: 1px; margin-top: 3px; }

  .mission .brand { left: 60px; top: 556px; }
  .mission .brand-mark { width: 52px; height: 52px; }
  .mission .brand-name { font-size: 30px; }

  .order-call {
    position: absolute; left: 20px; width: 287px; top: 626px; z-index: 2; text-align: center;
    font-family: "Marcellus", serif; font-size: 15px; line-height: 1.3; color: var(--ink);
  }

  .cover .brand { left: 40px; top: 40px; }
  .cover .brand-mark { width: 70px; height: 70px; }
  .cover .brand-name { font-size: 38px; }

  .tagline {
    position: absolute; left: 20px; width: 287px; top: 592px; z-index: 2; text-align: center;
    font-family: "Marcellus", serif; font-size: 17px; line-height: 1.3; color: var(--ink);
  }
  .tagline strong { font-family: "Lato", sans-serif; font-weight: 700; }
</style>
</head>
<body>
  <main class="brochure">
    <svg class="wave-art" viewBox="0 0 654 760">
      <defs>
        <clipPath id="intro-photo-clip">
          <path d="M0,255 H327 V470 C220,455 120,330 0,300 Z"/>
        </clipPath>
        <clipPath id="mission-photo-clip">
          <path d="M327,345 H654 V470 C560,472 440,476 327,470 Z"/>
        </clipPath>
      </defs>
      <rect role="img" aria-label="Photo of a newborn baby wrapped in a white blanket" x="0" y="255" width="327" height="225" fill="var(--photo-baby)" clip-path="url(#intro-photo-clip)"/>
      <rect role="img" aria-label="Photo of the founder, a smiling nurse seated by a bright window" x="327" y="345" width="327" height="135" fill="var(--photo-room)" clip-path="url(#mission-photo-clip)"/>
      <path d="M0,300 C120,330 220,455 340,472 S560,470 654,462" fill="none" stroke="var(--green)" stroke-width="22"/>
      <path d="M0,326 C110,372 220,488 350,498 S560,486 654,478" fill="none" stroke="var(--navy)" stroke-width="11"/>
      <circle cx="60" cy="420" r="28" fill="var(--navy)" opacity="0.45"/>
      <circle cx="82" cy="440" r="13" fill="var(--green-dark)" opacity="0.7"/>
      <circle cx="592" cy="486" r="30" fill="var(--sky)" opacity="0.7"/>
      <circle cx="612" cy="528" r="14" fill="var(--green)" opacity="0.8"/>
    </svg>

    <section class="panel intro">
      <h2 class="heading">Inspired by love</h2>
      <p class="body-copy">My love in helping babies and their parents during my over 30yrs of nursing experience are what inspired me to create Nestling Baby Products</p>
      <div class="social">
        <p class="social-title">Follow us:</p>
        <p class="social-line"><span class="social-dot"></span>/NestlingBabyCo</p>
        <p class="social-line"><span class="social-dot"></span>@nestlingbaby</p>
      </div>
      <p class="web">www.<b>nestlingbaby</b>.com</p>
      <div class="foot-bar"></div>
    </section>

    <section class="panel mission">
      <h2 class="heading">Empowering Parents</h2>
      <p class="body-copy">My goal has been to empower parents in making informed decisions for their baby's care. We specialize in promoting the bonding between parents and their babies while creating a safe and healthy environment for the baby's growth.</p>
      <div class="brand">
        <span class="brand-mark"></span>
        <span class="brand-name">Nestling<small>baby products</small></span>
      </div>
      <p class="order-call">FOR MORE INFORMATION AND<br>TO ORDER PLEASE VISIT</p>
      <p class="web">www.<b>nestlingbaby</b>.com</p>
      <div class="foot-bar"></div>
    </section>

    <section class="panel cover">
      <svg class="panel-art" viewBox="0 0 327 760">
        <circle cx="70" cy="200" r="24" fill="var(--green)" opacity="0.35"/>
        <circle cx="190" cy="290" r="124" fill="none" stroke="var(--sky)" stroke-width="8"/>
        <circle role="img" aria-label="Photo of a baby resting in a cushioned baby nest" cx="190" cy="290" r="118" fill="var(--photo-nest)"/>
        <circle cx="95" cy="460" r="58" fill="none" stroke="var(--sky)" stroke-width="6"/>
        <circle role="img" aria-label="Photo of a sleeping newborn close up" cx="95" cy="460" r="54" fill="var(--photo-nest)"/>
        <circle cx="215" cy="490" r="72" fill="none" stroke="var(--green)" stroke-width="7"/>
        <circle role="img" aria-label="Photo of a father resting beside his baby in a nest" cx="215" cy="490" r="68" fill="#e2ddd6"/>
        <circle cx="40" cy="520" r="20" fill="var(--green)" opacity="0.45"/>
      </svg>
      <div class="brand">
        <span class="brand-mark"></span>
        <span class="brand-name">Nestling<small>baby products</small></span>
      </div>
      <p class="tagline">Helping parents and caregivers to welcome new babies into <strong>safe, secure, and peaceful environments.</strong></p>
      <p class="web">www.<b>nestlingbaby</b>.com</p>
      <div class="foot-bar"></div>
    </section>
  </main>
</body>
</html>
```